依頼詳細
載内容詳細に関しては、別添のExcel資料を参照してください。

・ターゲット
BtoB
マンションの管理組合や管理業者
BtoC
防水工事系の仕事経験者の方で仕事を探している方

・カラーイメージ
青系
ロゴで使用されている青色を使用して、デザインお願いします。
▼参考
https://www.harumizu-cycle.jp/

・デザイン、ムード
参考のように企業らしい堅めのイメージでデザインお願いします
▼参考
http://www.tomonaga-kiko.biz
https://www.seiran-kenchi.co.jp/

配置やデザイン等はアレンジしていただいて構いません。
また、縦に制限はありません。

レスポンシブデザインのサイトで、bootstrap4を利用しコーディングする予定になります。

デザイン幅は2000px、コンテンツの幅はbootstrap4デフォルトのの1110pxを基準としてください。
ただし、最近のデザインの流行を取りいれて、フルワイドや、1200~1500px程度の幅のコンテンツをバランスよくレイアウトしてください。
コンテンツ配置は基本12分割になります。がデザインによっては、多少逸脱してもかまいません。
bootstrap4、12分割グリッドの基準のPSDも資料として添付しております。
ご参考になさってください。

本分のフォントはゴシック系は游ゴシック、メイリオ、明朝系は遊明朝でお願いします。
飾り文字はフリーフォントか、googleフォントを利用してください。

メイン画像部分・グローバルメニューは、ワイド適用でお願いします。

不明点、質問などありましたらメッセージ等でご連絡ください。
サイトURL
ページ数
1ページ
希望イメージ
シンプル 複雑
単色 カラフル
暗い 明るい
日常 高級
遊び心 厳粛
未来的 伝統的
女性的 男性的
希望する色
青系、水色系
納品ファイル
• 高解像度JPG (.jpg)
• フォトショップ形式 (.psd)
補足説明
・資料上はサイト名(社名)や住所などは伏字にしております。
ご提案時点ではそのまま作成をお願いします。

・使用画像は当選後こちらで用意します。
ご提案時点では前項同様に、カンプデータ等をご使用のうえ、当選後に本内容へ差し替え修正をお願いします。
また、雰囲気が合っていれば、指定外の画像を追加掲載いただいてOKです。

・当選前提となった方は正式な社名及び連絡先をお伝えしますので修正対応をお願いします。

お客様が希望されていたデザインイメージにピッタリだったため。

数多くの素晴らしい提案をいただきありがとうございました。
また次回もご参加よろしくお願いいたします。

```html
<!DOCTYPE html>
<html lang="ja">
<head>
<meta charset="utf-8">
<title>株式会社〇〇〇〇</title>
<link rel="stylesheet" href="https://fonts.googleapis.com/css2?family=Noto+Sans+JP:wght@400;500;700&family=Noto+Serif+JP:wght@500;700&display=swap">
<style>
:root{
  --navy:#173a84;
  --blue:#2a5cb0;
  --sky:#7fa6d8;
  --pale:#eef3fa;
  --line:#d4deec;
  --text:#3a4150;
  --muted:#8a93a3;
  --white:#ffffff;
  --footer:#2b57a8;
}
*{margin:0;padding:0;box-sizing:border-box}
html,body{width:1200px;height:2560px;overflow:hidden}
body{font-family:"Noto Sans JP",sans-serif;color:var(--text);background:var(--white);position:relative;font-size:13px}
.serif{font-family:"Noto Serif JP",serif}

/* hero */
.hero{position:absolute;left:0;top:0;width:1200px;height:540px;overflow:hidden}
.hero-photo{position:absolute;inset:0;
  background:
    radial-gradient(ellipse 260px 300px at 420px 330px,rgba(40,48,64,.55),rgba(40,48,64,0) 70%),
    radial-gradient(ellipse 200px 260px at 620px 320px,rgba(60,66,80,.45),rgba(60,66,80,0) 70%),
    radial-gradient(ellipse 220px 220px at 220px 300px,rgba(235,238,242,.9),rgba(235,238,242,0) 70%),
    linear-gradient(90deg,#c9d6e6 0%,#b4c6de 30%,#8fa8cb 55%,#d5e0ee 75%,#eef3f9 100%);}
.hero-curve{position:absolute;left:0;bottom:0;width:1200px;height:130px}
.brand{position:absolute;left:30px;top:22px;display:flex;align-items:center;gap:10px}
.brand-dot{width:30px;height:30px;border-radius:50%;background:var(--blue)}
.brand-name{font-size:18px;font-weight:700;color:var(--navy)}
.hero-copy{position:absolute;right:70px;top:330px;text-align:right;color:var(--navy);font-weight:700;line-height:1.5;font-size:40px;text-shadow:0 0 12px rgba(255,255,255,.9)}

/* nav */
.gnav{position:absolute;top:548px;left:0;width:1200px;height:56px;display:flex;align-items:center;justify-content:center}
.gnav ul{list-style:none;display:flex;gap:44px;margin-right:120px}
.gnav li{display:flex;align-items:center;gap:8px;font-size:14px;color:var(--navy);font-weight:500}
.gnav svg{width:16px;height:16px}
.tel-btn{position:absolute;right:40px;top:4px;width:210px;height:46px;border:2px solid var(--blue);background:var(--white);display:flex;flex-direction:column;justify-content:center;align-items:center}
.tel-btn .t1{font-size:11px;color:var(--navy)}
.tel-btn .t2{font-size:12px;font-weight:700;color:var(--white);background:var(--blue);padding:1px 10px;margin-top:3px}

/* headings */
.sec-title{position:absolute;left:0;width:1200px;text-align:center;color:var(--navy);font-weight:700;font-size:26px}
.sec-title .cap{font-size:38px;color:var(--blue)}
.sec-title::after{content:"";display:block;width:40px;height:2px;background:var(--blue);margin:8px auto 0}

/* about */
.about-text{position:absolute;top:755px;left:0;width:1200px;text-align:center;font-size:13px;line-height:2;color:var(--text)}
.about-scene{position:absolute;top:850px;left:150px;width:900px;height:170px;
  background:
    radial-gradient(ellipse 160px 90px at 180px 130px,rgba(140,175,220,.55),rgba(140,175,220,0) 70%),
    radial-gradient(ellipse 200px 110px at 470px 120px,rgba(120,160,215,.5),rgba(120,160,215,0) 70%),
    radial-gradient(ellipse 170px 95px at 760px 130px,rgba(150,185,225,.55),rgba(150,185,225,0) 70%),
    linear-gradient(180deg,#ffffff 0%,#f0f5fb 35%,#d6e3f3 75%,#c2d4ec 100%);}
.about-sign{position:absolute;top:1028px;right:160px;font-size:11px;color:var(--muted)}

/* services */
.services{position:absolute;top:1095px;left:150px;width:900px;display:flex;gap:15px}
.svc{flex:1}
.svc-img{height:195px;position:relative}
.svc-img.a{background:
    linear-gradient(180deg,rgba(60,66,76,.55) 0%,rgba(60,66,76,.25) 100%),
    linear-gradient(135deg,#8d97a6 0%,#b5bcc6 45%,#d6dadf 100%)}
.svc-img.b{background:
    radial-gradient(ellipse 120px 90px at 90px 110px,rgba(160,180,120,.55),rgba(160,180,120,0) 70%),
    linear-gradient(100deg,#a79d7c 0%,#cfc6a8 40%,#e4dfcc 70%,#c4b991 100%)}
.svc-img.c{background:
    radial-gradient(ellipse 110px 140px at 170px 100px,rgba(110,120,135,.55),rgba(110,120,135,0) 70%),
    linear-gradient(180deg,#9fbbe0 0%,#c6d6ea 50%,#8f9aa8 100%)}
.svc-img .over{position:absolute;left:0;right:0;top:70px;text-align:center;color:var(--white);font-size:13px;line-height:1.8}
.svc-label{height:38px;border:1px solid var(--line);border-top:3px solid var(--blue);display:flex;align-items:center;justify-content:center;font-size:14px;color:var(--navy);font-weight:500}

/* works */
.works-bg{position:absolute;top:1360px;left:0;width:1200px;height:620px;background:var(--pale)}
.tabs{position:absolute;top:1440px;left:150px;width:900px;display:flex;border-bottom:2px solid var(--blue)}
.tabs span{padding:6px 24px;font-size:13px;color:var(--navy)}
.tabs span.on{background:var(--blue);color:var(--white)}
.works{position:absolute;top:1490px;left:150px;width:900px;display:grid;grid-template-columns:repeat(4,1fr);gap:18px 16px}
.work-img{height:150px}
.w1{background:
    radial-gradient(ellipse 70px 80px at 70px 80px,rgba(70,80,95,.55),rgba(70,80,95,0) 70%),
    linear-gradient(180deg,#c9d6e6 0%,#e8edf3 55%,#9ea8b5 100%)}
.w2{background:
    radial-gradient(ellipse 90px 60px at 110px 60px,rgba(245,245,240,.9),rgba(245,245,240,0) 70%),
    linear-gradient(180deg,#b9cfe6 0%,#dfe6da 45%,#8ea676 100%)}
.w3{background:
    radial-gradient(ellipse 80px 60px at 60px 100px,rgba(150,170,110,.5),rgba(150,170,110,0) 70%),
    linear-gradient(110deg,#b3a883 0%,#d8d0b6 50%,#c2b68f 100%)}
.w4{background:
    radial-gradient(ellipse 80px 50px at 110px 50px,rgba(230,235,242,.8),rgba(230,235,242,0) 70%),
    linear-gradient(135deg,#6f7988 0%,#a8b0bb 55%,#d2d7dd 100%)}
.work-cap{font-size:11px;color:var(--text);padding-top:6px;height:28px}
.more{position:absolute;top:1895px;left:540px;width:120px;height:34px;background:var(--blue);color:var(--white);font-size:13px;display:flex;align-items:center;justify-content:center;gap:6px}

/* recruit */
.recruit-title{left:430px;width:440px;top:2010px}
.recruit-text{position:absolute;top:2110px;left:150px;width:360px;font-size:13px;line-height:1.9}
.recruit-text .lead{color:var(--navy);font-weight:700;font-size:15px;margin-bottom:6px}
.recruit-photo{position:absolute;top:2070px;left:530px;width:520px;height:240px;
  background:
    radial-gradient(ellipse 80px 120px at 300px 150px,rgba(225,230,238,.95),rgba(225,230,238,0) 70%),
    radial-gradient(ellipse 80px 120px at 410px 150px,rgba(70,78,92,.5),rgba(70,78,92,0) 70%),
    linear-gradient(90deg,#8fa6c6 0%,#b7c8e0 35%,#dfe7f2 60%,#c3d2e6 100%)}

/* footer */
.footer{position:absolute;top:2370px;left:0;width:1200px;height:190px;background:var(--footer);color:var(--white)}
.f-brand{position:absolute;top:38px;left:300px;display:flex;align-items:center;gap:10px}
.f-brand .brand-dot{background:var(--white);width:26px;height:26px}
.f-brand span{font-size:16px;font-weight:700}
.f-info{position:absolute;top:34px;left:620px;font-size:12px;line-height:1.9}
.f-nav{position:absolute;top:128px;left:0;width:1200px;display:flex;justify-content:center;gap:46px;font-size:12px;list-style:none}
</style>
</head>
<body>

<header class="hero">
  <div class="hero-photo" role="img" aria-label="ヘルメットを持った作業員と社員が並ぶ、ビル街を背景にした写真"></div>
  <svg class="hero-curve" viewBox="0 0 1200 130" preserveAspectRatio="none"><path d="M0 70 Q600 160 1200 40 L1200 130 L0 130 Z" fill="#ffffff"/></svg>
  <div class="brand"><span class="brand-dot"></span><span class="brand-name">株式会社〇〇〇〇</span></div>
  <div class="hero-copy serif"><div>安心安全の生活を</div><div>当たり前にするためのお手伝い</div></div>
</header>

<nav class="gnav">
  <ul>
    <li><svg viewBox="0 0 16 16"><path d="M2 8 L8 2 L14 8 V14 H2 Z" fill="#2a5cb0"/></svg>HOME</li>
    <li><svg viewBox="0 0 16 16"><rect x="2" y="3" width="12" height="10" fill="#2a5cb0"/></svg>業務内容</li>
    <li><svg viewBox="0 0 16 16"><rect x="2" y="2" width="12" height="12" fill="none" stroke="#2a5cb0" stroke-width="2"/></svg>施工事例</li>
    <li><svg viewBox="0 0 16 16"><rect x="3" y="2" width="10" height="12" fill="#2a5cb0"/></svg>会社案内</li>
    <li><svg viewBox="0 0 16 16"><rect x="1" y="3" width="14" height="10" fill="none" stroke="#2a5cb0" stroke-width="2"/><path d="M1 3 L8 9 L15 3" fill="none" stroke="#2a5cb0" stroke-width="2"/></svg>お問い合わせ</li>
  </ul>
  <div class="tel-btn"><span class="t1">お電話でのお問い合わせはこちら</span><span class="t2">TEL 000-0000-0000</span></div>
</nav>

<h2 class="sec-title serif" style="top:690px"><span class="cap">私</span>たちについて</h2>
<p class="about-text">〇〇〇〇は、大阪府を拠点に<br>防水工事・外壁補修工事を中心に、マンション管理組合様、管理会社様と共に建物を守り続けてきました。<br>確かな技術と誠実な対応で、住まう方々の安心安全な暮らしを支えてまいります。</p>
<div class="about-scene" role="img" aria-label="淡い青色で描かれた街並みのイラスト"></div>
<p class="about-sign">代表取締役　〇〇〇〇</p>

<h2 class="sec-title serif" style="top:1030px"><span class="cap">業</span>務内容</h2>
<section class="services">
  <div class="svc"><div class="svc-img a" role="img" aria-label="防水工事の施工面の写真"><p class="over">水回りのトラブルを解決し<br>快適な生活をご提案します。</p></div><div class="svc-label">防水工事</div></div>
  <div class="svc"><div class="svc-img b" role="img" aria-label="外壁補修作業の写真"></div><div class="svc-label">外壁補修工事</div></div>
  <div class="svc"><div class="svc-img c" role="img" aria-label="足場を組んだマンションの写真"></div><div class="svc-label">大規模修繕</div></div>
</section>

<div class="works-bg"></div>
<h2 class="sec-title serif" style="top:1375px"><span class="cap">施</span>工事例</h2>
<div class="tabs"><span class="on">すべて</span><span>防水工事</span><span>外壁補修工事</span><span>大規模修繕</span></div>
<section class="works">
  <div><div class="work-img w1" role="img" aria-label="屋上で作業する職人の写真"></div><p class="work-cap">〇〇マンション様 防水工事</p></div>
  <div><div class="work-img w2" role="img" aria-label="完成した建物外観の写真"></div><p class="work-cap">〇〇マンション様 外壁補修</p></div>
  <div><div class="work-img w3" role="img" aria-label="外壁補修の施工写真"></div><p class="work-cap">〇〇マンション様 外壁補修</p></div>
  <div><div class="work-img w4" role="img" aria-label="防水施工面の写真"></div><p class="work-cap">〇〇マンション様 防水工事</p></div>
  <div><div class="work-img w1" role="img" aria-label="屋上で作業する職人の写真"></div><p class="work-cap">〇〇マンション様 防水工事</p></div>
  <div><div class="work-img w2" role="img" aria-label="完成した建物外観の写真"></div><p class="work-cap">〇〇マンション様 外壁補修</p></div>
  <div><div class="work-img w3" role="img" aria-label="外壁補修の施工写真"></div><p class="work-cap">〇〇マンション様 外壁補修</p></div>
  <div><div class="work-img w4" role="img" aria-label="防水施工面の写真"></div><p class="work-cap">〇〇マンション様 防水工事</p></div>
</section>
<div class="more">MORE <svg width="10" height="10" viewBox="0 0 10 10"><path d="M3 1 L7 5 L3 9" fill="none" stroke="#fff" stroke-width="1.6"/></svg></div>

<h2 class="sec-title serif recruit-title"><span class="cap">採</span>用情報</h2>
<div class="recruit-text">
  <p class="lead">〇〇〇〇では、</p>
  <p>意欲ある方と共に未来を築いてまいります。経験を活かし、地域の暮らしを支える仕事に〇〇〇〇で挑戦しませんか。</p>
</div>
<div class="recruit-photo" role="img" aria-label="ビルを背景に立つ作業着姿の社員の写真"></div>

<footer class="footer">
  <div class="f-brand"><span class="brand-dot"></span><span>株式会社〇〇〇〇</span></div>
  <div class="f-info">〒000-0000　〇〇県〇〇市〇〇町0-0-0<br>TEL 000-0000-0000　FAX 000-0000-0000</div>
  <ul class="f-nav"><li>HOME</li><li>業務内容</li><li>施工事例</li><li>会社案内</li><li>採用情報</li><li>お問い合わせ</li></ul>
</footer>

</body>
</html>
```